Organic Coconut oil

A label for a 500ml jar of organic coconut oil
The product is raw cold pressed virgin coconut oil
Target Market(s)
All health conscious individuals
Industry/Entity Type
Product
Requirements
Must have
- Virgin
Raw
Cold pressed
Organic
Product name tovi coconut oil

```html
<!DOCTYPE html>
<html lang="en">
<head>
<meta charset="utf-8">
<title>Tovi Coconut Oil – 500ml Jar Label</title>
<link rel="stylesheet" href="https://fonts.googleapis.com/css2?family=Bebas+Neue&family=Playfair+Display:ital,wght@1,700&display=swap">
<style>
  :root {
    --canvas: #ffffff;
    --frame-light: #b4744c;
    --frame-dark: #6e3d24;
    --cream: #fbe9dc;
    --cream-line: #f6dccb;
    --ink-brown: #7a4026;
    --sky-glow: #f7b069;
    --sky-mid: #d9885a;
    --sky-deep: #8e5239;
    --palm-shadow: #2b1710;
  }

  * { box-sizing: border-box; margin: 0; padding: 0; }

  html, body {
    width: 1200px;
    height: 849px;
    overflow: hidden;
    background: var(--canvas);
  }

  .canvas {
    position: relative;
    width: 1200px;
    height: 849px;
  }

  .jar-label {
    position: absolute;
    left: 240px;
    top: 180px;
    width: 720px;
    height: 490px;
    border-radius: 34px;
    background: linear-gradient(180deg, var(--frame-light), var(--frame-dark));
    box-shadow: 0 10px 18px rgba(0, 0, 0, 0.25);
  }

  .label-inner {
    position: absolute;
    inset: 20px;
    border-radius: 22px;
    border: 4px solid var(--cream-line);
    overflow: hidden;
  }

  .sunset-photo {
    position: absolute;
    inset: 0;
    background:
      radial-gradient(ellipse 260px 200px at 8% 88%, var(--palm-shadow) 0%, rgba(43, 23, 16, 0.85) 45%, rgba(43, 23, 16, 0) 100%),
      radial-gradient(ellipse 220px 320px at 22% 45%, rgba(43, 23, 16, 0.9) 0%, rgba(43, 23, 16, 0) 75%),
      radial-gradient(ellipse 300px 140px at 10% 95%, var(--sky-glow) 0%, rgba(247, 176, 105, 0) 70%),
      linear-gradient(180deg, var(--sky-deep) 0%, var(--sky-mid) 45%, var(--sky-glow) 100%);
  }

  .brand-name {
    position: absolute;
    left: 250px;
    top: 18px;
    width: 330px;
    font-family: "Bebas Neue", sans-serif;
    font-weight: 400;
    font-size: 54px;
    line-height: 0.9;
    color: var(--cream);
    text-align: center;
  }

  .claims {
    position: absolute;
    right: 24px;
    top: 136px;
    list-style: none;
    display: flex;
    flex-direction: column;
    align-items: flex-end;
    gap: 20px;
  }

  .claim {
    display: inline-block;
    background: var(--cream);
    color: var(--ink-brown);
    font-family: "Bebas Neue", sans-serif;
    font-size: 40px;
    line-height: 1;
    padding: 2px 8px 0;
  }

  .volume-band {
    position: absolute;
    left: 0;
    right: 0;
    bottom: 34px;
    height: 30px;
    background: var(--cream);
    display: flex;
    align-items: center;
    padding-left: 18px;
  }

  .volume {
    font-family: "Playfair Display", serif;
    font-style: italic;
    font-weight: 700;
    font-size: 22px;
    color: var(--palm-shadow);
  }
</style>
</head>
<body>
  <main class="canvas">
    <section class="jar-label">
      <div class="label-inner">
        <div class="sunset-photo" role="img" aria-label="Photograph of coconut palm silhouettes against an orange tropical sunset sky"></div>
        <h1 class="brand-name">Tovi<br>Coconut Oil</h1>
        <ul class="claims">
          <li class="claim">Raw</li>
          <li class="claim">Organic</li>
          <li class="claim">Cold Pressed</li>
          <li class="claim">Virgin Coconut Oil</li>
        </ul>
        <div class="volume-band">
          <span class="volume">500ml</span>
        </div>
      </div>
    </section>
  </main>
</body>
</html>
```